SaaS Early tech startup business card design

Unique design for experience ecommerce platform company. the business cards will be used by executive members. conformance with color code is required.

```html
<!DOCTYPE html>
<html lang="en">
<head>
<meta charset="utf-8">
<title>Korvel Business Card</title>
<link rel="stylesheet" href="https://fonts.googleapis.com/css2?family=Inter:wght@400;500;700;800&display=swap">
<style>
  :root {
    --bg: #3b3b3c;
    --paper: #ffffff;
    --navy: #0d5e87;
    --teal: #14b39f;
    --teal-bright: #03c2b0;
    --deep-blue: #055f8f;
    --ink: #555a5e;
    --mark-grey: #4a4a4c;
  }
  * { margin: 0; padding: 0; box-sizing: border-box; }
  html, body {
    width: 1200px; height: 1200px; overflow: hidden;
    background: var(--bg);
    font-family: "Inter", "Helvetica Neue", Arial, sans-serif;
  }
  .card {
    position: absolute;
    left: 262px;
    width: 686px;
    height: 392px;
    overflow: hidden;
  }
  .card--front { top: 165px; background: var(--paper); }
  .card--back {
    top: 653px;
    background: linear-gradient(180deg, var(--teal-bright) 0%, #04a0ab 45%, var(--deep-blue) 100%);
  }
  .wordmark {
    position: absolute;
    font-weight: 800;
    letter-spacing: -2px;
    line-height: 1;
    white-space: nowrap;
  }
  .card--front .wordmark {
    right: 41px; top: 40px;
    font-size: 80px;
    color: #0a6b8f;
  }
  .card--back .wordmark {
    left: 0; right: 0; top: 128px;
    text-align: center;
    font-size: 124px;
    color: var(--mark-grey);
  }
  .person { position: absolute; left: 40px; top: 219px; }
  .person__name {
    font-size: 24px; font-weight: 700; color: var(--navy);
    letter-spacing: 0.2px; line-height: 1.1;
  }
  .person__role {
    font-size: 16px; font-weight: 400; color: var(--teal);
    line-height: 1.2; margin-top: 1px;
  }
  .contacts {
    position: absolute; left: 40px; top: 283px;
    display: grid;
    grid-template-columns: 150px auto;
    row-gap: 4px;
    font-size: 15.5px; color: var(--ink);
  }
  .contact { display: flex; align-items: center; gap: 9px; height: 17px; }
  .contact svg { width: 13px; height: 14px; flex: none; fill: var(--teal); }
  .address-band {
    position: absolute; left: 0; right: 0; top: 338px; height: 26px;
    background: linear-gradient(90deg, #0b6e93 0%, #0b6e93 3%, #0aa3a2 7%, #00bfa8 30%, #00bfa8 58%, #0a8ea0 80%, #0d6a92 100%);
    color: #ffffff;
    font-size: 15.5px;
    line-height: 26px;
    padding-left: 38px;
  }
</style>
</head>
<body>

<section class="card card--front" aria-label="Business card front">
  <div class="wordmark">korvel</div>

  <div class="person">
    <div class="person__name">DANIEL REYES</div>
    <div class="person__role">President</div>
  </div>

  <div class="contacts">
    <div class="contact">
      <svg viewBox="0 0 14 14" aria-hidden="true"><path d="M3 1l2.2 2.8-1.2 1.5c.8 1.7 2 2.9 3.7 3.7l1.5-1.2L12 10l-1.6 2.6C5.6 12.3 1.7 8.4 1.4 3.6z"/></svg>
      <span>555-214-7390</span>
    </div>
    <div class="contact">
      <svg viewBox="0 0 14 14" aria-hidden="true"><path d="M4 0h6a1 1 0 0 1 1 1v12a1 1 0 0 1-1 1H4a1 1 0 0 1-1-1V1a1 1 0 0 1 1-1zm.6 1.6v9h4.8v-9z"/></svg>
      <span>hello@korvel.io</span>
    </div>
    <div class="contact">
      <svg viewBox="0 0 14 14" aria-hidden="true"><path d="M3.5 0h7a1 1 0 0 1 1 1v12a1 1 0 0 1-1 1h-7a1 1 0 0 1-1-1V1a1 1 0 0 1 1-1zm.7 1.5v9.5h5.6V1.5zM7 11.8a.7.7 0 1 0 0 1.4.7.7 0 0 0 0-1.4z"/></svg>
      <span>555-618-2043</span>
    </div>
    <div class="contact">
      <svg viewBox="0 0 14 14" aria-hidden="true"><path d="M7 1a6 6 0 1 0 0 12A6 6 0 0 0 7 1zm-1 2.2c.8.4 1 1.3.4 1.9-.7.6-1.7.3-2 1.2-.3.8.8 1.3.6 2.2-.2.7-1 .6-1.4 1.1A4.7 4.7 0 0 1 6 3.2zm3.2 7.6c-.5-.4-.2-1.1-.7-1.6-.6-.5-1.6-.2-1.7-1-.1-.7.8-1 1.5-.9.8.1 1.4-.3 1.6-1 .3.6.5 1.3.5 2 0 1-.5 1.9-1.2 2.5z"/></svg>
      <span>www.korvel.io</span>
    </div>
  </div>

  <div class="address-band">1420 Harbor Crest Road, Juneau, Alaska 99801</div>
</section>

<section class="card card--back" aria-label="Business card back">
  <div class="wordmark">korvel</div>
</section>

</body>
</html>
```